Brightwave Reach - Business Card

We need a business card for a Social Media Marketing company that specializes in online marketing for small businesses in Canada using common Social Media platforms such as Pictora, Kinloop, Blinkit & Chirpo.

I have uploaded a copy of our logo which I would like utilized in the business card. We would like the business card to be modern yet classy design.

Our website is www.brightwavereach.ca

Industry/Entity Type

Marketing

Contact Information for Business Card

Email: info@brightwavereach.ca
Website: www.brightwavereach.ca
Telephone: 604-392-5108

Colors

Designer to choose colors to be used in the design.

Requirements
Must have
• Social Media icons on reverse
• Please add some designs with color.

```html
<!DOCTYPE html>
<html lang="en">
<head>
<meta charset="utf-8">
<title>Brightwave Reach – Business Card</title>
<link rel="stylesheet" href="https://fonts.googleapis.com/css2?family=Oswald:wght@500&family=Playfair+Display:wght@800;900&display=swap">
<style>
  :root {
    --canvas: #dcd7cf;
    --card: #070707;
    --pattern: #242424;
    --red: #e3232b;
    --white: #ffffff;
    --muted: #1d1d1d;
  }
  * { box-sizing: border-box; margin: 0; padding: 0; }
  html, body { width: 1200px; height: 675px; overflow: hidden; }
  body {
    background: var(--canvas);
    display: grid;
    grid-template-columns: repeat(2, 500px);
    grid-template-rows: repeat(2, 286px);
    gap: 30px 40px;
    justify-content: center;
    align-content: center;
    font-family: "Playfair Display", Georgia, serif;
  }
  .card {
    position: relative;
    width: 500px;
    height: 286px;
    background: var(--card);
    overflow: hidden;
  }

  /* Bands */
  .band { position: absolute; top: 208px; height: 14px; }
  .band--short { left: 0; width: 124px; clip-path: polygon(0 0, 100% 0, 94% 100%, 0 100%); }
  .band--long  { left: 140px; right: 0; clip-path: polygon(1.6% 0, 100% 0, 100% 100%, 0 100%); }
  .band--red { background: var(--red); }
  .band--white { background: var(--white); }

  /* Front */
  .front__pattern {
    position: absolute; left: 0; top: 0; width: 170px; height: 208px;
    background: linear-gradient(100deg, var(--pattern) 0%, #181818 55%, rgba(7,7,7,0) 100%);
    clip-path: polygon(0 0, 88% 0, 70% 100%, 0 100%);
  }
  .front__name {
    position: absolute; left: 250px; top: 62px; width: 220px;
    color: var(--white); font-weight: 900; font-size: 30px; line-height: 1.05;
    text-align: center; letter-spacing: 0.5px; text-transform: uppercase;
  }
  .front__web {
    position: absolute; right: 42px; top: 245px;
    color: var(--muted); font-weight: 800; font-size: 12px; letter-spacing: 0.5px;
    text-transform: uppercase;
  }

  /* Back */
  .back__name {
    position: absolute; left: 26px; top: 22px;
    color: var(--white); font-weight: 900; font-size: 11px; line-height: 1.1;
    text-transform: uppercase; text-align: center;
  }
  .back__contact {
    position: absolute; left: 190px; width: 250px; top: 140px;
    color: var(--white); font-weight: 800; font-size: 13px; line-height: 1.45;
    text-align: center; text-transform: uppercase; letter-spacing: 0.3px;
    font-style: normal;
  }
  .networks {
    position: absolute; top: 240px; display: flex; align-items: center; list-style: none;
    font-family: "Oswald", "Arial Narrow", sans-serif; font-weight: 500; font-size: 9.5px;
  }
  .networks li { display: flex; align-items: center; gap: 3px; }
  .networks li::before { content: ""; width: 7px; height: 7px; border-radius: 50%; background: currentColor; }
  .networks--primary { left: 18px; gap: 9px; color: var(--red); }
  .networks--more { left: 146px; right: 18px; justify-content: space-between; color: var(--white); }
</style>
</head>
<body>

  <section class="card front" aria-label="Card front">
    <div class="front__pattern" role="img" aria-label="Faint pattern of social network symbols"></div>
    <h1 class="front__name">Brightwave<br>Reach</h1>
    <div class="band band--short band--white"></div>
    <div class="band band--long band--red"></div>
    <p class="front__web">www.brightwavereach.ca</p>
  </section>

  <section class="card back" aria-label="Card back">
    <p class="back__name">Brightwave<br>Reach</p>
    <address class="back__contact">info@brightwavereach.ca<br>www.brightwavereach.ca<br>604-392-5108</address>
    <div class="band band--short band--red"></div>
    <div class="band band--long band--white"></div>
    <ul class="networks networks--primary"><li>Kinloop</li><li>Pictora</li></ul>
    <ul class="networks networks--more">
      <li>Chirpo</li><li>Tunely</li><li>Reelo</li><li>Pinlore</li>
      <li>Worknet</li><li>Streamo</li><li>Circly</li><li>Blogro</li>
    </ul>
  </section>

  <section class="card back" aria-label="Card back">
    <p class="back__name">Brightwave<br>Reach</p>
    <address class="back__contact">info@brightwavereach.ca<br>www.brightwavereach.ca<br>604-392-5108</address>
    <div class="band band--short band--red"></div>
    <div class="band band--long band--white"></div>
    <ul class="networks networks--primary"><li>Kinloop</li><li>Pictora</li></ul>
    <ul class="networks networks--more">
      <li>Chirpo</li><li>Tunely</li><li>Reelo</li><li>Pinlore</li>
      <li>Worknet</li><li>Streamo</li><li>Circly</li><li>Blogro</li>
    </ul>
  </section>

  <section class="card front" aria-label="Card front">
    <div class="front__pattern" role="img" aria-label="Faint pattern of social network symbols"></div>
    <p class="front__name">Brightwave<br>Reach</p>
    <div class="band band--short band--white"></div>
    <div class="band band--long band--red"></div>
    <p class="front__web">www.brightwavereach.ca</p>
  </section>

</body>
</html>
```